Landing Page for pellowick.ca Design To Inspire Confidence Playfulness and Optimised for Conversion

A Landing Page that will have a cheery playful demeanor all the while inspiring confidence to customers to trust us when they are shipping their used or broken electronics to us.
We are a startup looking to scale up our operations and we recently have been working on a website pellowick.ca. We want to improve on our current landing page. Competition includes tarnbloom.com , http://www.quorvela.com/ , spindrel.com but spindrel operates a little different then us.
We've done a bit of research and found the current landing page is not suited for conversions.
We want the design to work within our current landing page design and not interfere with major programing. So where the pictures of the phones are, beneath the search bar, we want the background changed and replaced with a creative call to action to click one of the devices to continue towards getting a quote and for this background to be appealing. Also we wanted to make the rest of the page beneath that more appealing and professional. A big issue for us is making sure whatever design is submitted can be easily integrated using our current platform.
We will try and answer any questions as promptly as possible and encourage it.
Updates
Industry/Entity Type
Shipping
Number of Pages Required
1 page
Look and feel
Each slider illustrates characteristics of the customer's brand and the style your logo design should communicate.

```html
<!DOCTYPE html>
<html lang="en">
<head>
<meta charset="utf-8">
<title>Pellowick – Sell Your Phone</title>
<link rel="stylesheet" href="https://fonts.googleapis.com/css2?family=Open+Sans:wght@400;600;700;800&display=swap">
<style>
:root{
  --blue:#0a8ef0;
  --blue-bright:#1396f5;
  --ink:#1c1c1c;
  --muted:#6b6b6b;
  --faint:#b9b9b9;
  --band:#f4f4f4;
  --line:#e3e3e3;
  --hero-panel:#5a5a5a;
  --yellow:#f2f20a;
  --cta-band:#0b2740;
  --footer:#06111e;
  --white:#ffffff;
}
*{box-sizing:border-box;margin:0;padding:0}
html,body{width:995px;height:1200px;overflow:hidden;background:var(--white)}
body{font-family:"Open Sans",Arial,sans-serif;color:var(--ink)}
.page{position:relative;width:995px;height:1200px;overflow:hidden}
.abs{position:absolute}

/* header */
.site-header{position:absolute;left:0;top:0;width:995px;height:48px;background:var(--white)}
.brand{position:absolute;left:174px;top:10px;font-weight:800;font-size:25px;letter-spacing:.5px;color:var(--ink)}
.main-nav{position:absolute;top:17px;right:173px;display:flex;gap:40px;font-size:10px;color:var(--muted)}

/* hero */
.hero{position:absolute;left:0;top:48px;width:995px;height:221px}
.hero-photo{position:absolute;left:0;top:0;width:601px;height:221px;background:linear-gradient(100deg,#3e3e3e 0%,#6c6a68 45%,#8d8b88 70%,#4b4b4d 100%)}
.hero-panel{position:absolute;left:601px;top:0;width:394px;height:221px;background:var(--hero-panel)}
.hero-copy{position:absolute;left:173px;top:42px;color:var(--white)}
.hero-title{font-weight:800;font-size:26px;line-height:1.1;letter-spacing:.3px}
.hero-title .accent{display:block;color:var(--yellow);font-size:34px}
.hero-lead{margin-top:12px;font-weight:700;font-size:11px;line-height:1.55}
.hero-lead .free{color:var(--yellow)}
.testimonial-avatar{position:absolute;left:617px;top:73px;width:38px;height:38px;border-radius:50%;background:linear-gradient(#c9a98b,#7c6250)}
.testimonial-name{position:absolute;left:671px;top:77px;color:var(--white);font-size:15px}
.testimonial-place{position:absolute;left:672px;top:97px;color:#e0e0e0;font-size:8px}
.testimonial-quote{position:absolute;left:616px;top:118px;width:205px;color:var(--white);font-size:15px;line-height:1.35}
.hero-dots{position:absolute;left:617px;top:194px;display:flex;gap:10px;align-items:center}
.dot{width:6px;height:6px;border-radius:50%;background:var(--white)}
.dot.active{width:13px;height:13px;background:var(--blue)}

/* stats */
.stats{position:absolute;left:0;top:269px;width:995px;height:55px;background:var(--band)}
.stats-number{position:absolute;left:390px;top:6px;font-size:36px;color:var(--blue)}
.stats-label{position:absolute;left:506px;top:15px;font-size:11px;line-height:1.3}
.stats-label b{font-weight:600}

/* how it works */
.section-title{position:absolute;left:0;width:995px;text-align:center;font-weight:600;font-size:20px;top:347px}
.steps-line{position:absolute;left:276px;top:403px;width:442px;height:3px;background:var(--line)}
.step-dot{position:absolute;top:396px;width:17px;height:17px;border-radius:50%;background:#dadada}
.step-dot.active{background:var(--blue)}
.step{position:absolute;top:420px;width:180px;text-align:center}
.step h3{font-size:12px;font-weight:700}
.step p{margin-top:6px;font-size:7.5px;line-height:1.45;color:#444}

/* quote box */
.quote-box{position:absolute;left:174px;top:511px;width:647px;height:138px;border:1px solid #d8d8d8;background:var(--white)}
.quote-side{position:absolute;left:0;top:0;width:150px;height:136px;background:#f6f6f6}
.quote-side h2{position:absolute;left:17px;top:13px;font-size:13px;font-weight:600}
.quote-steps{position:absolute;left:17px;top:40px;list-style:none;font-size:7px;line-height:13px;color:var(--faint)}
.quote-steps .current{color:var(--blue);font-weight:600}
.device-label{position:absolute;left:167px;top:15px;font-size:8px;color:var(--muted)}
.device{position:absolute;top:40px;width:80px;text-align:center;font-size:9px;color:#333}
.device svg{display:block;margin:0 auto 8px}

/* testimonials */
.reviews{position:absolute;left:0;top:746px;width:995px;height:273px;background:var(--blue-bright);color:var(--white)}
.reviews h2{position:absolute;left:173px;top:20px;font-size:15px;font-weight:700}
.review{position:absolute;width:200px;font-size:8px;line-height:16px}
.review b{font-weight:700}
.reviews-dots{position:absolute;left:463px;top:238px;display:flex;gap:9px;align-items:center}
.reviews-dots .dot.active{width:13px;height:13px;background:var(--white)}

/* cta */
.cta-band{position:absolute;left:0;top:1019px;width:995px;height:83px;background:var(--cta-band)}
.cta-text{position:absolute;left:289px;top:32px;color:var(--white);font-size:15px;font-weight:700}
.cta-button{position:absolute;left:545px;top:20px;width:165px;height:43px;background:var(--blue);color:var(--white);font-weight:700;font-size:14px;display:flex;align-items:center;justify-content:center}

/* footer */
.site-footer{position:absolute;left:0;top:1102px;width:995px;height:98px;background:var(--footer);color:var(--white)}
.copyright{position:absolute;left:173px;top:59px;font-size:7px;font-weight:700}
.footer-nav{position:absolute;right:173px;top:59px;display:flex;gap:22px;font-size:7.5px}
</style>
</head>
<body>
<div class="page">

  <header class="site-header">
    <div class="brand">PELLOWICK</div>
    <nav class="main-nav"><span>How it Works</span><span>Track My Offers</span><span>Login</span><span>Contact</span></nav>
  </header>

  <section class="hero">
    <div class="hero-photo" role="img" aria-label="Photo of a young man in glasses sitting on a couch using a laptop"></div>
    <div class="hero-panel"></div>
    <div class="hero-copy">
      <h1 class="hero-title">SELL YOUR PHONE<span class="accent">WITHOUT SELLING!</span></h1>
      <p class="hero-lead">YES! Just sit on your couch, we will pick up your phone,<br>and send you the money.<br>And it's <span class="free">FREE!!!</span></p>
    </div>
    <div class="testimonial-avatar" role="img" aria-label="Customer portrait"></div>
    <div class="testimonial-name">A. Vellacourt</div>
    <div class="testimonial-place">Southriver, NT.</div>
    <p class="testimonial-quote">“ An amazing service that is well needed. To sell your phone online with such ease. ”</p>
    <div class="hero-dots"><span class="dot active"></span><span class="dot"></span><span class="dot"></span><span class="dot"></span><span class="dot"></span></div>
  </section>

  <section class="stats">
    <div class="stats-number">45.000</div>
    <div class="stats-label"><b>Sales in Pellowick</b><br>and still counting!</div>
  </section>

  <h2 class="section-title">How it works</h2>
  <div class="steps-line"></div>
  <span class="step-dot active" style="left:268px"></span>
  <span class="step-dot" style="left:489px"></span>
  <span class="step-dot" style="left:710px"></span>
  <div class="step" style="left:186px"><h3>Get a Quote</h3><p>Select your device, tell the conditions,<br>then we will offer the price</p></div>
  <div class="step" style="left:407px"><h3>Pick Up</h3><p>We will pick up your phone, or you can<br>ship it then we pay the shipping.</p></div>
  <div class="step" style="left:628px"><h3>Get Paid</h3><p>We mail you hard cash, or choose an<br>Marketvale gift card and get a bonus.</p></div>

  <section class="quote-box">
    <div class="quote-side">
      <h2>Get a Quote</h2>
      <ol class="quote-steps">
        <li class="current">1. Select Your Device</li>
        <li>2. Select Device Model</li>
        <li>3. Select Provider</li>
        <li>4. Select Model Type</li>
        <li>5. Tell it's Condition</li>
        <li>6. You Get The Quote</li>
      </ol>
    </div>
    <div class="device-label">Select Your Device</div>
    <div class="device" style="left:141px">
      <svg width="36" height="66" viewBox="0 0 36 66"><rect x="1" y="1" width="34" height="64" rx="4" fill="#111"/><rect x="3" y="8" width="30" height="48" fill="#fff"/><circle cx="18" cy="31" r="6" fill="#bbb"/></svg>Orbphones</div>
    <div class="device" style="left:233px">
      <svg width="36" height="66" viewBox="0 0 36 66"><rect x="1" y="1" width="34" height="64" rx="4" fill="#111"/><rect x="3" y="8" width="30" height="48" fill="#fff"/><circle cx="18" cy="31" r="6" fill="#6cbf3a"/></svg>Droidlines</div>
    <div class="device" style="left:324px">
      <svg width="36" height="66" viewBox="0 0 36 66"><rect x="1" y="1" width="34" height="64" rx="3" fill="#111"/><rect x="3" y="6" width="30" height="54" fill="#fff"/><circle cx="18" cy="31" r="5" fill="#111"/></svg>Kestrels</div>
    <div class="device" style="left:416px">
      <svg width="46" height="66" viewBox="0 0 46 66"><rect x="1" y="1" width="44" height="64" rx="4" fill="#111"/><rect x="4" y="5" width="38" height="52" fill="#fff"/><circle cx="23" cy="31" r="6" fill="#bbb"/><circle cx="23" cy="61" r="2" fill="#fff"/></svg>Tabrix</div>
    <div class="device" style="left:508px">
      <svg width="28" height="66" viewBox="0 0 28 66"><rect x="1" y="8" width="26" height="50" rx="3" fill="#111"/><rect x="5" y="12" width="18" height="14" fill="#fff"/><circle cx="14" cy="43" r="8" fill="#fff"/><circle cx="14" cy="43" r="3" fill="#111"/></svg>Tunebox</div>
  </section>

  <section class="reviews">
    <h2>Bunch of Satisfied Pellowickers!</h2>
    <p class="review" style="left:173px;top:56px">“ Best thing that every happened to me to help me pay off my contract and start fresh. ”<br><b>Derek Hallom</b> - Toronto, ON</p>
    <p class="review" style="left:394px;top:56px">“ Thanks thanks thanks, Ill be back to sell my daughters phone. ”<br><b>Derek Hallom</b> - Milton, ON</p>
    <p class="review" style="left:615px;top:56px">“ Please tell me how I just got paid this much. ”<br><b>Nora Quill</b> - Brooks, AB</p>
    <p class="review" style="left:173px;top:137px">“ Thanks amazing service will surely recommend. ”<br><b>Owen Marsh</b> - Nort York, ON</p>
    <p class="review" style="left:394px;top:137px">“ I'm not sure why I didnt find this sooner, seriously. ”<br><b>Lena Brightwell</b> - Calgary, AB</p>
    <p class="review" style="left:615px;top:137px">“ Corvex contracts are meaningless now that we can just sell my entire families phones and just pay off the contract and still be left with cash for new phones. ”<br><b>Tobin Ferro</b> - Toronto, ON</p>
    <div class="reviews-dots"><span class="dot active"></span><span class="dot"></span><span class="dot"></span><span class="dot"></span><span class="dot"></span></div>
  </section>

  <section class="cta-band">
    <div class="cta-text">Sell Your Phone Without Efforts!</div>
    <div class="cta-button">START NOW</div>
  </section>

  <footer class="site-footer">
    <div class="copyright">© 2014 PELLOWICK. ALL RIGHTS RESERVED</div>
    <nav class="footer-nav"><span>Home</span><span>How it Works</span><span>Track My Offers</span><span>Business</span><span>Login</span><span>Contact</span><span>FQ</span><span>Terms &amp; Conditions</span></nav>
  </footer>

</div>
</body>
</html>
```